Simple menu needed for Asian food truck

We are an Asian food truck that attends big festivals. Our menu is very simple featuring only about 5 or 6 dishes, but we need big pictures and lettering to capture the attention of festival goers. Our motto is "Fresh, Authentic, Homemade", it would be great to include that somewhere. We also need a menu that possibly magnetic so that we can easily take off items that are sold out, change pricing or add different dishes for specific venues. Attached is an example of what our current menu looks like.

```html
<!DOCTYPE html>
<html lang="en">
<head>
<meta charset="utf-8">
<title>Jade Lantern – Festival Menu</title>
<link rel="stylesheet" href="https://fonts.googleapis.com/css2?family=Arimo:wght@400;700&display=swap">
<style>
  :root {
    --page: #ffffff;
    --panel: #fdc9c9;
    --band: #fe9797;
    --plate: #e3e3e3;
    --plate-edge: #b9b9b9;
    --pill-top: #cc2a6c;
    --pill-bottom: #a1273f;
    --tea-band: #c93399;
    --ink: #0d0d0d;
    --white: #ffffff;
  }
  * { box-sizing: border-box; margin: 0; padding: 0; }
  html, body { width: 1200px; height: 1200px; overflow: hidden; background: var(--page); }
  body { font-family: "Arimo", Arial, sans-serif; color: var(--ink); position: relative; }

  .menu-board { position: absolute; left: 173px; top: 43px; width: 854px; height: 1134px; background: var(--panel); }

  .menu-item { position: absolute; left: 0; width: 854px; height: 120px; }
  .item-band { position: absolute; left: 200px; right: 60px; top: 16px; height: 87px; background: var(--band);
    box-shadow: 0 4px 6px rgba(150, 60, 60, .25); }
  .item-name { position: absolute; left: 225px; width: 410px; top: 0; height: 120px;
    display: flex; flex-direction: column; justify-content: center; align-items: center; text-align: center; line-height: 1.05; }
  .item-name strong { font-size: 38px; font-weight: 700; letter-spacing: .3px; }
  .item-name span { font-size: 25px; font-weight: 400; margin-top: 2px; }
  .item-plate { position: absolute; left: 32px; top: 2px; width: 199px; height: 114px; }
  .item-photo { position: absolute; border-radius: 40%; }
  .price-pill { position: absolute; left: 640px; top: 8px; width: 181px; height: 104px; border-radius: 52px;
    background: linear-gradient(var(--pill-top), var(--pill-bottom)); color: var(--white);
    display: flex; justify-content: center; align-items: center; box-shadow: 0 4px 8px rgba(120, 20, 50, .3); }
  .price-pill span { display: block; text-align: center; font-weight: 700; font-size: 38px; line-height: 1.05; }

  .tea-band { position: absolute; left: 0; top: 783px; width: 854px; height: 193px; background: var(--tea-band); }
  .tea-title { position: absolute; left: 71px; top: 30px; color: var(--white); font-size: 62px; font-weight: 700; }
  .tea-flavours { position: absolute; left: 69px; top: 115px; display: flex; gap: 9px; }
  .tea-flavour { height: 45px; border: 3px solid var(--white); border-radius: 12px; color: var(--white);
    font-size: 29px; font-weight: 700; display: flex; align-items: center; justify-content: center; }
  .tea-photo { position: absolute; left: 591px; top: 817px; width: 223px; height: 286px; border-radius: 14px;
    background: linear-gradient(90deg, #d8323d 0%, #e4584a 48%, #ef9a3c 52%, #f2b04c 100%); }

  .brand-name { position: absolute; left: 60px; top: 1050px; width: 140px; text-align: center;
    font-weight: 700; font-size: 24px; line-height: 1.1; color: var(--ink); }
  .payment-processor { position: absolute; left: 260px; top: 1010px; width: 107px; height: 31px; background: var(--white);
    display: flex; align-items: center; justify-content: center; font-size: 18px; }
  .payment-cards { position: absolute; left: 216px; top: 1046px; display: flex; gap: 4px; }
  .payment-card { width: 47px; height: 35px; background: var(--white); border: 1px solid #c9c9c9;
    display: flex; align-items: center; justify-content: center; font-size: 9px; font-weight: 700; color: var(--ink); }
</style>
</head>
<body>
<main class="menu-board">

  <section class="menu-item" style="top:55px">
    <div class="item-band"></div>
    <svg class="item-plate" viewBox="0 0 199 114"><ellipse cx="99" cy="62" rx="98" ry="51" fill="var(--plate-edge)"/><ellipse cx="99" cy="55" rx="98" ry="51" fill="var(--plate)"/></svg>
    <div class="item-photo" role="img" aria-label="Plate of golden fried chicken eggrolls" style="left:65px;top:-8px;width:125px;height:92px;background:radial-gradient(#e0a24a,#b86a22 70%,transparent 72%)"></div>
    <div class="item-name"><strong>Chicken Eggrolls</strong></div>
    <div class="price-pill"><span>3 for<br>$6</span></div>
  </section>

  <section class="menu-item" style="top:192px">
    <div class="item-band"></div>
    <svg class="item-plate" viewBox="0 0 199 114"><ellipse cx="99" cy="62" rx="98" ry="51" fill="var(--plate-edge)"/><ellipse cx="99" cy="55" rx="98" ry="51" fill="var(--plate)"/></svg>
    <div class="item-photo" role="img" aria-label="Two fresh shrimp spring rolls in rice paper" style="left:45px;top:15px;width:180px;height:60px;background:linear-gradient(90deg,#f0c7b8,#cfe3c7,#f2b9a5,#9cc88b)"></div>
    <div class="item-name"><strong>Fresh Springrolls</strong><span>(Shrimp or Veggie)</span></div>
    <div class="price-pill"><span>2 for<br>$6</span></div>
  </section>

  <section class="menu-item" style="top:333px">
    <div class="item-band"></div>
    <svg class="item-plate" viewBox="0 0 199 114"><ellipse cx="99" cy="62" rx="98" ry="51" fill="var(--plate-edge)"/><ellipse cx="99" cy="55" rx="98" ry="51" fill="var(--plate)"/></svg>
    <div class="item-photo" role="img" aria-label="Two glazed Chinese BBQ pork skewers" style="left:60px;top:-35px;width:90px;height:150px;background:linear-gradient(160deg,#b8323a,#7a1a22 60%,#c49a6c)"></div>
    <div class="item-name"><strong>Chinese BBQ Pork<br>Skewers</strong></div>
    <div class="price-pill"><span>2 for<br>$6</span></div>
  </section>

  <section class="menu-item" style="top:475px">
    <div class="item-band"></div>
    <svg class="item-plate" viewBox="0 0 199 114"><ellipse cx="99" cy="62" rx="98" ry="51" fill="var(--plate-edge)"/><ellipse cx="99" cy="55" rx="98" ry="51" fill="var(--plate)"/></svg>
    <div class="item-photo" role="img" aria-label="Bowl of fried rice with meat and vegetables" style="left:55px;top:6px;width:150px;height:82px;background:radial-gradient(#c9a974,#a88b5a 60%,#f4f4f4 62%)"></div>
    <div class="item-name"><strong>Fried Rice</strong><span>Chicken or Pork</span></div>
    <div class="price-pill"><span>$5<br>Bowl</span></div>
  </section>

  <section class="menu-item" style="top:616px">
    <div class="item-band"></div>
    <svg class="item-plate" viewBox="0 0 199 114"><ellipse cx="99" cy="62" rx="98" ry="51" fill="var(--plate-edge)"/><ellipse cx="99" cy="55" rx="98" ry="51" fill="var(--plate)"/></svg>
    <div class="item-photo" role="img" aria-label="Stuffed chicken wing served with fried rice" style="left:25px;top:0;width:170px;height:95px;background:linear-gradient(170deg,#bfa271 0%,#a58a5c 55%,#c17a3a 75%,#8a4a1e)"></div>
    <div class="item-name"><strong>Angel Wing</strong><span>(Stuffed Chicken Wing)</span></div>
    <div class="price-pill"><span>$8<br>Combo</span></div>
  </section>

  <section class="tea-band">
    <h2 class="tea-title">Flavored Tea $5</h2>
    <div class="tea-flavours">
      <span class="tea-flavour" style="width:193px">Stowberry</span>
      <span class="tea-flavour" style="width:137px">Mango</span>
      <span class="tea-flavour" style="width:138px">Peach</span>
    </div>
  </section>
  <div class="tea-photo" role="img" aria-label="Two glasses of iced strawberry and peach tea with strawberries"></div>

  <div class="brand-name">Jade Lantern</div>
  <div class="payment-processor">Tillnova</div>
  <div class="payment-cards">
    <span class="payment-card">CardOne</span>
    <span class="payment-card">CardTwo</span>
    <span class="payment-card">CardThree</span>
    <span class="payment-card">CardFour</span>
  </div>
</main>
</body>
</html>
```